We are a doctors medical practice
I need the business card to be eye catching and memorable,
to reflect professionalism, yet also warmth and care

the numbers need to be easy to see, for the elderly

and the logo also in a location that is large enough to see and be eye catching

Back of card:
opening hours:
Mon- Fri 8.30am to 6pm
Sat 9am to 4pm

rows for appontments, date and time
Updates

HiĀ 

Modification to company name

BROOKVALE KINDRED HEALTH MEDICAL PRACTICE

Thanks
Marla

Reason: I am look for a unique design that also fulfils the design brief

I have attempted to post a .eps and .ai file of the logo

Target Market(s)

needs to appeal to the majority, mainly adults

Industry/Entity Type

Medical

Contact Information for Business Card

company name: Brookvale Kindred Health Medical Practice
Name: Dr Marla Vossberg-Tait
Qualifications: MBBS, Bsci(med), FRACGP, DCH, SH&FPA, Dip Derm
Address: Shop 3/41-43 Quorrow St, Brookvale 2940
Ph: 02 9418 3052
Fax: 02 9461 8824

Requirements
Nice to have
• I like balance
gold/ silver incorporated, as well as the other colours in the logo- but not limited to these colours
a "medical" feel
Should not have
• dark or strong colours

```html
<!DOCTYPE html>
<html lang="en">
<head>
<meta charset="utf-8">
<title>Brookvale Kindred Health Medical Practice – Business Card Colourways</title>
<link rel="stylesheet" href="https://fonts.googleapis.com/css2?family=Maven+Pro:wght@500;600&family=Tinos&display=swap">
<style>
  :root {
    --stage: #333333;
    --card: #ffffff;
    --green: #6cc04a;
    --pink: #f172aa;
    --blue: #1a9ad9;
    --brand-blue: #3a7cc4;
    --ring: #2e9bd6;
    --text-on-accent: #ffffff;
  }
  * { margin: 0; padding: 0; box-sizing: border-box; }
  html, body {
    width: 1200px;
    height: 2420px;
    overflow: hidden;
    background: var(--stage);
  }
  .card {
    position: absolute;
    left: 70px;
    width: 1063px;
    height: 655px;
    background: var(--card);
    overflow: hidden;
  }
  .card--green { top: 168px; --accent: var(--green); }
  .card--pink  { top: 879px; --accent: var(--pink); }
  .card--blue  { top: 1600px; --accent: var(--blue); }

  .card__panel {
    position: absolute;
    inset: 0;
    width: 1063px;
    height: 655px;
  }
  .card__panel circle { fill: var(--accent); }

  .brand {
    position: absolute;
    left: 66px;
    top: 136px;
    width: 300px;
    text-align: center;
    font-family: "Maven Pro", sans-serif;
    font-weight: 500;
    color: var(--brand-blue);
  }
  .brand__mark {
    display: block;
    width: 188px;
    height: 188px;
    margin: 0 auto 20px;
    border-radius: 50%;
    border: 10px solid var(--ring);
  }
  .brand__name {
    font-size: 27px;
    line-height: 35px;
  }

  .details {
    position: absolute;
    left: 557px;
    top: 0;
    width: 404px;
    color: var(--text-on-accent);
  }
  .details__name {
    position: absolute;
    top: 118px;
    left: 0;
    font-family: "Maven Pro", sans-serif;
    font-weight: 600;
    font-size: 34px;
    letter-spacing: 1px;
    white-space: nowrap;
  }
  .details__quals {
    position: absolute;
    top: 174px;
    right: 0;
    width: 260px;
    text-align: right;
    font-family: "Tinos", serif;
    font-size: 15px;
    line-height: 26px;
  }
  .details__rule {
    position: absolute;
    top: 232px;
    left: 0;
    width: 404px;
    height: 4px;
    background: var(--text-on-accent);
  }
  .details__label,
  .details__value {
    position: absolute;
    left: 0;
    font-family: "Tinos", serif;
    white-space: nowrap;
  }
  .details__label { font-size: 27px; }
  .details__value { font-size: 17px; letter-spacing: 0.5px; }
  .details__label--address { top: 260px; }
  .details__value--address { top: 306px; }
  .details__label--phone   { top: 338px; }
  .details__value--phone   { top: 389px; }
  .details__label--fax     { top: 415px; }
  .details__value--fax     { top: 463px; }
</style>
</head>
<body>

<section class="card card--green" aria-label="Business card, green colourway">
  <svg class="card__panel" viewBox="0 0 1063 655" aria-hidden="true">
    <defs>
      <filter id="edge-shadow-green" x="-20%" y="-20%" width="140%" height="140%">
        <feDropShadow dx="-3" dy="2" stdDeviation="5" flood-color="#000" flood-opacity="0.25"/>
      </filter>
    </defs>
    <circle cx="921" cy="284" r="485" stroke="#ffffff" stroke-width="9" filter="url(#edge-shadow-green)"/>
  </svg>
  <div class="brand">
    <span class="brand__mark"></span>
    <p class="brand__name">Kindred Health<br>Medical Brookvale</p>
  </div>
  <div class="details">
    <h1 class="details__name">Dr Marla Vossberg-Tait</h1>
    <p class="details__quals">MBBS, Bsci(med), FRACGP, DCH,<br>SH&amp;FPA, Dip Derm</p>
    <div class="details__rule"></div>
    <p class="details__label details__label--address">Address:-</p>
    <p class="details__value details__value--address">Shop 3/41-43 Quorrow St, Brookvale 2940</p>
    <p class="details__label details__label--phone">Phone:-</p>
    <p class="details__value details__value--phone">02 9418 3052</p>
    <p class="details__label details__label--fax">Fax:-</p>
    <p class="details__value details__value--fax">02 9461 8824</p>
  </div>
</section>

<section class="card card--pink" aria-label="Business card, pink colourway">
  <svg class="card__panel" viewBox="0 0 1063 655" aria-hidden="true">
    <defs>
      <filter id="edge-shadow-pink" x="-20%" y="-20%" width="140%" height="140%">
        <feDropShadow dx="-3" dy="2" stdDeviation="5" flood-color="#000" flood-opacity="0.25"/>
      </filter>
    </defs>
    <circle cx="921" cy="284" r="485" stroke="#ffffff" stroke-width="9" filter="url(#edge-shadow-pink)"/>
  </svg>
  <div class="brand">
    <span class="brand__mark"></span>
    <p class="brand__name">Kindred Health<br>Medical Brookvale</p>
  </div>
  <div class="details">
    <h1 class="details__name">Dr Marla Vossberg-Tait</h1>
    <p class="details__quals">MBBS, Bsci(med), FRACGP, DCH,<br>SH&amp;FPA, Dip Derm</p>
    <div class="details__rule"></div>
    <p class="details__label details__label--address">Address:-</p>
    <p class="details__value details__value--address">Shop 3/41-43 Quorrow St, Brookvale 2940</p>
    <p class="details__label details__label--phone">Phone:-</p>
    <p class="details__value details__value--phone">02 9418 3052</p>
    <p class="details__label details__label--fax">Fax:-</p>
    <p class="details__value details__value--fax">02 9461 8824</p>
  </div>
</section>

<section class="card card--blue" aria-label="Business card, blue colourway">
  <svg class="card__panel" viewBox="0 0 1063 655" aria-hidden="true">
    <defs>
      <filter id="edge-shadow-blue" x="-20%" y="-20%" width="140%" height="140%">
        <feDropShadow dx="-3" dy="2" stdDeviation="5" flood-color="#000" flood-opacity="0.25"/>
      </filter>
    </defs>
    <circle cx="921" cy="284" r="485" stroke="#ffffff" stroke-width="9" filter="url(#edge-shadow-blue)"/>
  </svg>
  <div class="brand">
    <span class="brand__mark"></span>
    <p class="brand__name">Kindred Health<br>Medical Brookvale</p>
  </div>
  <div class="details">
    <h1 class="details__name">Dr Marla Vossberg-Tait</h1>
    <p class="details__quals">MBBS, Bsci(med), FRACGP, DCH,<br>SH&amp;FPA, Dip Derm</p>
    <div class="details__rule"></div>
    <p class="details__label details__label--address">Address:-</p>
    <p class="details__value details__value--address">Shop 3/41-43 Quorrow St, Brookvale 2940</p>
    <p class="details__label details__label--phone">Phone:-</p>
    <p class="details__value details__value--phone">02 9418 3052</p>
    <p class="details__label details__label--fax">Fax:-</p>
    <p class="details__value details__value--fax">02 9461 8824</p>
  </div>
</section>

</body>
</html>
```